Bref créative
Edgy modern Letterhead an B. card for jet charter company
Veltaro Corporation
Professional
Peter Haldane
Founder, Chief Pilot
246 W. Harbor Ave., Suite 2020
Long Beach, CA 90815
855.5.VELTARO
phal@veltaro-example.com
veltaro-example.com
Use: Veltaro Corporation for company name

```html
<!DOCTYPE html>
<html lang="en">
<head>
<meta charset="utf-8">
<title>Veltaro Corporation — Stationery</title>
<link rel="stylesheet" href="https://fonts.googleapis.com/css2?family=Josefin+Sans:wght@300;400&family=Open+Sans:wght@400;600&display=swap">
<style>
  :root {
    --backdrop: #e6e6e6;
    --paper: #ffffff;
    --ink: #222222;
    --ink-soft: #666666;
    --band-dark: #2e2e2e;
    --band-mid: #5a5a5a;
    --plane-faint: #dcdcdc;
  }
  * { margin: 0; padding: 0; box-sizing: border-box; }
  html, body { width: 1200px; height: 936px; overflow: hidden; background: var(--backdrop); }
  body { position: relative; font-family: "Open Sans", Arial, sans-serif; color: var(--ink); }

  .sheet { position: absolute; background: var(--paper); overflow: hidden; }
  .wordmark { font-family: "Josefin Sans", Arial, sans-serif; font-weight: 300; color: var(--ink); line-height: 1; white-space: nowrap; }
  .web { font-size: 11px; letter-spacing: 0.08em; color: var(--ink-soft); white-space: nowrap; }

  /* Letterhead */
  .letterhead { left: 132px; top: 30px; width: 446px; height: 587px; }
  .letterhead .wordmark { position: absolute; left: 30px; top: 48px; font-size: 44px; }
  .letterhead .contact { position: absolute; left: 296px; top: 34px; font-size: 8px; line-height: 13px; color: var(--ink-soft); list-style: none; }
  .letterhead .contact li { display: flex; align-items: center; gap: 5px; white-space: nowrap; }
  .letterhead .contact .dot { width: 6px; height: 6px; border-radius: 50%; background: var(--band-mid); flex: none; }
  .letterhead .plane-faint { position: absolute; left: 140px; top: 292px; width: 230px; height: 40px; background: var(--plane-faint); border-radius: 20px 6px 6px 20px; }
  .band { position: absolute; left: 0; bottom: 0; width: 100%; height: 46px; }
  .letterhead .web { position: absolute; right: 24px; bottom: 54px; }

  /* Folder */
  .folder { left: 634px; top: 30px; width: 465px; height: 587px; }
  .folder .wordmark { position: absolute; left: 0; width: 100%; top: 242px; text-align: center; font-size: 110px; }
  .folder .web { position: absolute; right: 24px; bottom: 54px; }

  /* Business cards */
  .card-front { left: 30px; top: 736px; width: 203px; height: 81px; }
  .card-front .wordmark { position: absolute; left: 12px; top: 10px; font-size: 24px; }
  .card-front .person { position: absolute; left: 12px; top: 44px; font-size: 6px; line-height: 8px; color: var(--ink-soft); white-space: nowrap; }
  .card-front .person strong { color: var(--ink); font-weight: 600; }
  .card-front .details { position: absolute; right: 10px; top: 44px; font-size: 6px; line-height: 8px; color: var(--ink-soft); text-align: right; white-space: nowrap; }
  .card-back { left: 30px; top: 830px; width: 203px; height: 81px; background: var(--band-dark); border-radius: 6px; }
  .card-back .plane { position: absolute; left: 66px; top: 28px; width: 72px; height: 16px; background: #ececec; border-radius: 8px 3px 3px 8px; }
  .card-back .web { position: absolute; left: 0; width: 100%; bottom: 8px; text-align: center; font-size: 6px; color: #bbbbbb; }

  /* Envelopes */
  .envelope-front { left: 264px; top: 736px; width: 434px; height: 175px; }
  .envelope-front .wordmark { position: absolute; left: 20px; top: 20px; font-size: 34px; }
  .envelope-back { left: 733px; top: 736px; width: 432px; height: 175px; }
  .envelope-back .flap { position: absolute; left: 0; top: 0; width: 100%; height: 100px; }
  .envelope-back .web { position: absolute; left: 0; width: 100%; top: 22px; text-align: center; font-size: 16px; color: #ffffff; letter-spacing: 0.06em; }
</style>
</head>
<body>

<section class="sheet letterhead">
  <div class="wordmark">veltaro</div>
  <ul class="contact">
    <li><span class="dot"></span>246 W. Harbor Ave., Suite 2020</li>
    <li><span class="dot"></span>Seaview, CA 90815</li>
    <li><span class="dot"></span>562.555.0100</li>
    <li><span class="dot"></span>T 562.555.0142</li>
    <li><span class="dot"></span>F 562.555.0187</li>
    <li><span class="dot"></span>peter@veltaro-example.com</li>
    <li><span class="dot"></span>veltaro-example.com</li>
  </ul>
  <div class="plane-faint" role="img" aria-label="Faint silhouette of a private jet"></div>
  <div class="web">www.veltaro-example.com</div>
  <svg class="band" viewBox="0 0 446 46" preserveAspectRatio="none">
    <path d="M0 14 H200 C230 14 235 0 265 0 H446 V46 H0 Z" fill="var(--band-mid)"/>
    <path d="M0 22 H205 C235 22 240 8 270 8 H446 V46 H0 Z" fill="var(--band-dark)"/>
  </svg>
</section>

<section class="sheet folder">
  <div class="wordmark">veltaro</div>
  <div class="web">www.veltaro-example.com</div>
  <svg class="band" viewBox="0 0 465 46" preserveAspectRatio="none">
    <path d="M0 14 H210 C240 14 245 0 275 0 H465 V46 H0 Z" fill="var(--band-mid)"/>
    <path d="M0 22 H215 C245 22 250 8 280 8 H465 V46 H0 Z" fill="var(--band-dark)"/>
  </svg>
</section>

<section class="sheet card-front">
  <div class="wordmark">veltaro</div>
  <div class="person"><strong>Peter Haldane</strong><br>Founder, Chief Pilot<br>246 W. Harbor Ave., Suite 2020<br>Seaview, CA 90815</div>
  <div class="details">562.555.0100<br>peter@veltaro-example.com<br>veltaro-example.com</div>
</section>

<section class="sheet card-back">
  <div class="plane" role="img" aria-label="Silhouette of a private jet"></div>
  <div class="web">www.veltaro-example.com</div>
</section>

<section class="sheet envelope-front">
  <div class="wordmark">veltaro</div>
</section>

<section class="sheet envelope-back">
  <svg class="flap" viewBox="0 0 432 100" preserveAspectRatio="none">
    <path d="M0 0 H432 V60 L300 96 Q216 112 132 96 L0 60 Z" fill="var(--band-dark)"/>
  </svg>
  <div class="web">www.veltaro-example.com</div>
</section>

</body>
</html>
```